Exciting new aperitif brand needs a great label

Vel-Doro is a wonderful rich new premium-priced bitter aperitif, with a deep red colour, from a 100+ year old distillery (1890) near Turin in the Piedmont region of Italy. Inspired by Tessoli, it is perfectly formulated to elevate the classic Negroni cocktail (and variations on it). It also goes perfectly in a Spritz or a long mixed drink with soda or tonic. The name Vel-Doro is derived from the French for 'peak' and the Italian word for 'love'.

The label, which should take inspiration from Tessoli, but be distinctively different, can incoporate any number of premium label embellishments (foil, embossing, textures etc) and should be no greater than 11cm (height) x 9cm (width) with any core imagery restricted to a width of c.7cm.

The attached mood board should act as inspiration and colour should largely be restricted to reds, blues, whites and perhaps orange. For completeness, the label should note that the ABV is 25% and the bottle size 70cl.

Target Market(s)

21-45yr olds - equal split female/male

Colors
0054AA
0677BA
7BADD7
CADEEF
E8F1F8
0094D4
00A9DD
6FCCEA
C7EBF8
E9F6FB
EE7325
F08F49
F5BC92
FAE3D3
FDF4ED
EB3D1F
EC4F4E
F09395
F8D3D4
FCEDEE

Requirements
Must have
• Great lettering design on the name Vel-Doro

```html
<!DOCTYPE html>
<html lang="en">
<head>
<meta charset="utf-8">
<title>Vel-Doro Label</title>
<link rel="stylesheet" href="https://fonts.googleapis.com/css2?family=Oswald:wght@700&family=Orbitron:wght@500;600&display=swap">
<style>
  :root {
    --backdrop: #c4c4c4;
    --label-white: #f7f7f8;
    --gold: #c99a2e;
    --gold-light: #e6c463;
    --brand-red: #c4161c;
    --muted-grey: #9a9a9a;
    --sun-deep: #e89a2c;
    --sun-pale: #f8d9a0;
  }
  * { margin: 0; padding: 0; box-sizing: border-box; }
  html, body {
    width: 1200px;
    height: 2230px;
    overflow: hidden;
    background: var(--backdrop);
  }
  .canvas {
    position: relative;
    width: 1200px;
    height: 2230px;
  }
  .label {
    position: absolute;
    left: 150px;
    top: 508px;
    width: 900px;
    height: 1215px;
    filter: drop-shadow(0 10px 18px rgba(0,0,0,0.18));
  }
  .label-shape {
    position: absolute;
    inset: 0;
  }
  .label-text {
    position: absolute;
    left: 0;
    width: 100%;
    text-align: center;
  }
  .since {
    top: 172px;
    font-family: "Orbitron", sans-serif;
    font-weight: 600;
    font-size: 34px;
    letter-spacing: 2px;
    color: var(--gold);
  }
  .brand-name {
    top: 250px;
    font-family: "Oswald", sans-serif;
    font-weight: 700;
    font-size: 170px;
    line-height: 1;
    color: var(--brand-red);
    letter-spacing: 2px;
  }
  .tagline {
    top: 458px;
    font-family: "Orbitron", sans-serif;
    font-weight: 500;
    font-size: 29px;
    color: var(--muted-grey);
    letter-spacing: 1px;
  }
  .tagline .divider {
    display: inline-block;
    margin: 0 14px;
    font-size: 24px;
    vertical-align: 2px;
  }
  .scene-art {
    position: absolute;
    left: 259px;
    top: 594px;
    width: 382px;
    height: 272px;
    border-radius: 191px 191px 0 0;
    background: linear-gradient(180deg, var(--sun-pale) 0%, #f3c47a 55%, var(--sun-deep) 100%);
  }
  .volume {
    top: 944px;
    font-family: "Orbitron", sans-serif;
    font-weight: 600;
    font-size: 54px;
    color: var(--gold);
  }
</style>
</head>
<body>
  <main class="canvas">
    <section class="label">
      <svg class="label-shape" width="900" height="1215" viewBox="0 0 900 1215" aria-hidden="true">
        <defs>
          <linearGradient id="frameGold" x1="0" y1="0" x2="0" y2="1">
            <stop offset="0" stop-color="#d9ab3c"/>
            <stop offset="0.55" stop-color="#e6c463" stop-opacity="0.9"/>
            <stop offset="1" stop-color="#e6c463" stop-opacity="0"/>
          </linearGradient>
        </defs>
        <path d="M0 146 C 140 96, 260 0, 450 0 C 640 0, 760 96, 900 146 V1215 H0 Z" fill="#f7f7f8"/>
        <path d="M30 600 V178 C 160 130, 275 34, 450 34 C 625 34, 740 130, 870 178 V600"
              fill="none" stroke="url(#frameGold)" stroke-width="4"/>
      </svg>

      <p class="label-text since">SINCE: 1890</p>
      <h1 class="label-text brand-name">VEL-DORO</h1>
      <p class="label-text tagline">Premium Quality<span class="divider">|</span>ABV is 25%</p>
      <div class="scene-art" role="img" aria-label="Watercolour desert scene with sun above golden dunes"></div>
      <p class="label-text volume">70cl</p>
    </section>
  </main>
</body>
</html>
```